Brand and Programs Diagram

We want to present our Brands and Programs in a diagram.

Attached are a couple of examples of ideas of how we see it could be presented
Logos all attached
Similar colours and fonts

Instructions
Maple Grove Kindergarten logo In the middle and biggest
Feeds to
a heading in top right
Bloom Pathway 2.0 Curriculum
then five pillars below and their logos
Keen Steps
Curious
Gather
Move
Tribe

Then to the left
Have a heading
Brands & Programs

Have lines feeding from the Maple Grove Kindergarten logo to each of the Brand & Programs logos

Kestrel

Nest +

Tots +

DOVE

WREN

If there is a way of colour coding shading or making the DOVE, WREN, and Tribe logos connect in some way would be ideal as they are all part of the same family

At the very top if we could add the Maple Grove Education logo and have it feed into the Maple Grove Kindergarten logo.

```html
<!DOCTYPE html>
<html lang="en">
<head>
<meta charset="utf-8">
<title>Maple Grove — Brands &amp; Programs</title>
<link rel="stylesheet" href="https://fonts.googleapis.com/css2?family=Poppins:wght@400;600;700;800&display=swap">
<style>
:root{
  --sky:#00adee;
  --page:#e9e9e9;
  --card:#ffffff;
  --ring:#e6e6e6;
  --ink:#2f2f2f;
  --rule:#dcdcdc;
  --bracket:#3a3a3a;
  --green:#8dc63f;
  --blue:#1b9ad6;
  --orange:#f6a21b;
  --red:#ef4136;
  --forest:#2a9d48;
  --amber:#f7941d;
  --scarlet:#ed1c24;
  --crimson:#c4161c;
}
*{margin:0;padding:0;box-sizing:border-box}
html,body{width:1200px;height:871px;overflow:hidden;background:var(--page);font-family:"Poppins",sans-serif;color:var(--ink)}
.board{position:relative;width:1200px;height:871px}
.diagram{position:absolute;left:0;top:0}
.heading{position:absolute;top:72px;font-weight:800;font-size:22px;color:#fff;letter-spacing:-.2px;text-transform:uppercase;white-space:nowrap;transform:translateX(-50%)}
.heading--brands{left:246px}
.heading--curriculum{left:933px}
.mark{position:absolute;color:#fff;font-weight:700;text-align:center;transform:translate(-50%,-50%);line-height:1.1}
.mark--education{left:591px;top:150px;font-size:17px;width:160px}
.mark--kindergarten{left:601px;top:404px;font-size:30px;width:240px}
.mark--kestrel{left:367px;top:233px;font-size:17px}
.mark--wren{left:368px;top:709px;font-size:17px}
.mark--dove{left:320px;top:602px;font-size:14px}
.mark--nest,.mark--tots{color:var(--ink);font-weight:400;font-size:16px}
.mark--nest{left:312px;top:368px}
.mark--tots{left:302px;top:488px}
.item{position:absolute;width:230px;font-size:14.2px;line-height:16.5px}
.item--left{text-align:right}
.item h3{font-size:13.5px;font-weight:700;text-transform:uppercase;margin-bottom:8px;line-height:14px}
.kestrel h3{color:var(--green)}
.nest h3,.tots h3,.keen h3{color:var(--blue)}
.dove h3{color:var(--orange)}
.wren h3{color:var(--red)}
.curious h3{color:var(--forest)}
.gather h3{color:var(--amber)}
.move h3{color:var(--scarlet)}
.tribe h3{color:var(--crimson)}
</style>
</head>
<body>
<div class="board">
<svg class="diagram" width="1200" height="871" viewBox="0 0 1200 871">
  <rect x="28" y="35" width="1143" height="808" fill="var(--card)"/>
  <rect x="28" y="35" width="1143" height="93" fill="var(--sky)"/>
  <rect x="28" y="836" width="1143" height="7" fill="var(--sky)"/>
  <circle cx="591" cy="105" r="108" fill="#dedede"/>
  <circle cx="591" cy="105" r="105" fill="var(--sky)"/>
  <rect x="480" y="35" width="222" height="93" fill="var(--sky)"/>

  <g fill="none" stroke-width="1.2" stroke-dasharray="1.5 2">
    <path d="M412 233H576V254" stroke="var(--green)"/>
    <path d="M791 233H628V254" stroke="var(--blue)"/>
    <path d="M370 367H455" stroke="var(--blue)"/>
    <path d="M361 489H472" stroke="var(--blue)"/>
    <path d="M747 366H835" stroke="var(--forest)"/>
    <path d="M727 489H836" stroke="var(--amber)"/>
    <path d="M368 601H525V534" stroke="var(--orange)"/>
    <path d="M836 603H686V529" stroke="var(--scarlet)"/>
    <path d="M413 708H573V553" stroke="var(--red)"/>
    <path d="M791 709H628V553" stroke="var(--crimson)"/>
  </g>
  <g>
    <circle cx="576" cy="233" r="3.5" fill="var(--green)"/>
    <circle cx="628" cy="233" r="3.5" fill="var(--blue)"/>
    <circle cx="399" cy="367" r="3.5" fill="var(--blue)"/>
    <circle cx="404" cy="489" r="3.5" fill="var(--blue)"/>
    <circle cx="780" cy="366" r="3.5" fill="var(--forest)"/>
    <circle cx="783" cy="489" r="3.5" fill="var(--amber)"/>
    <circle cx="525" cy="601" r="3.5" fill="var(--orange)"/>
    <circle cx="686" cy="603" r="3.5" fill="var(--scarlet)"/>
    <circle cx="573" cy="708" r="3.5" fill="var(--red)"/>
    <circle cx="628" cy="709" r="3.5" fill="var(--crimson)"/>
  </g>

  <path d="M303 643H88V784H837V754M365 754V784" fill="none" stroke="var(--bracket)" stroke-width="1.3"/>

  <circle cx="601" cy="404" r="151" fill="var(--sky)"/>
  <circle cx="601" cy="404" r="146" fill="#fff"/>
  <circle cx="601" cy="404" r="140" fill="var(--sky)"/>

  <g stroke="var(--ring)" stroke-width="5">
    <circle cx="367" cy="233" r="42" fill="var(--sky)"/>
    <circle cx="325" cy="367" r="42" fill="#fff"/>
    <circle cx="316" cy="488" r="42" fill="#fff"/>
    <circle cx="323" cy="602" r="42" fill="#fff"/>
    <circle cx="368" cy="709" r="42" fill="var(--sky)"/>
    <circle cx="836" cy="233" r="42" fill="#fff"/>
    <circle cx="879" cy="367" r="42" fill="#fff"/>
    <circle cx="880" cy="488" r="42" fill="#fff"/>
    <circle cx="880" cy="602" r="42" fill="#fff"/>
    <circle cx="836" cy="709" r="42" fill="#fff"/>
  </g>
  <circle cx="346" cy="367" r="6" fill="var(--blue)"/>
  <circle cx="341" cy="486" r="6" fill="var(--blue)"/>
  <rect x="291" y="589" width="58" height="27" fill="var(--sky)"/>

  <defs>
    <linearGradient id="g-books" x1="0" y1="0" x2="0" y2="1"><stop offset="0" stop-color="#f6c343"/><stop offset=".5" stop-color="#e5433a"/><stop offset="1" stop-color="#2a8fd6"/></linearGradient>
    <radialGradient id="g-play"><stop offset="0" stop-color="#f9d423"/><stop offset="1" stop-color="#4aa3df"/></radialGradient>
    <linearGradient id="g-hands" x1="0" x2="1"><stop offset="0" stop-color="#f9d12c"/><stop offset="1" stop-color="#f47c20"/></linearGradient>
    <linearGradient id="g-heart" x1="0" y1="0" x2="0" y2="1"><stop offset="0" stop-color="#ed1c24"/><stop offset="1" stop-color="#f9d423"/></linearGradient>
    <linearGradient id="g-team" x1="0" x2="1"><stop offset="0" stop-color="#f2c21b"/><stop offset=".5" stop-color="#c4161c"/><stop offset="1" stop-color="#3ab54a"/></linearGradient>
  </defs>
  <circle cx="836" cy="233" r="32" fill="url(#g-books)" role="img" aria-label="Illustration of a stack of colourful books"/>
  <circle cx="879" cy="367" r="32" fill="url(#g-play)" role="img" aria-label="Illustration of colourful play beads"/>
  <circle cx="880" cy="488" r="32" fill="url(#g-hands)" role="img" aria-label="Illustration of two hands forming a heart"/>
  <circle cx="880" cy="602" r="32" fill="url(#g-heart)" role="img" aria-label="Illustration of a heart with fruit"/>
  <circle cx="836" cy="709" r="36" fill="url(#g-team)" role="img" aria-label="Illustration of people joined in a circle"/>
</svg>

<div class="heading heading--brands">Brands &amp; Programs</div>
<div class="heading heading--curriculum">Bloom Pathway 2.0 Curriculum</div>

<div class="mark mark--education">Maple Grove Education</div>
<div class="mark mark--kindergarten">Maple Grove Kindergarten</div>
<div class="mark mark--kestrel">Kestrel</div>
<div class="mark mark--nest">Nest</div>
<div class="mark mark--tots">Tots</div>
<div class="mark mark--dove">DOVE</div>
<div class="mark mark--wren">WREN</div>

<div class="item item--left kestrel" style="left:83px;top:207px"><h3>Kestrel</h3><p>Lorem ipsum dolor sit amet,<br>consectetur adipiscing elit, sed</p></div>
<div class="item item--left nest" style="left:39px;top:339px"><h3>Nest +</h3><p>Lorem ipsum dolor sit amet,<br>consectetur adipiscing elit, sed</p></div>
<div class="item item--left tots" style="left:31px;top:461px"><h3>Tots +</h3><p>Lorem ipsum dolor sit amet,<br>consectetur adipiscing elit, sed</p></div>
<div class="item item--left dove" style="left:26px;top:575px"><h3>DOVE</h3><p>Lorem ipsum dolor sit amet,<br>consectetur adipiscing elit, sed</p></div>
<div class="item item--left wren" style="left:83px;top:682px"><h3>WREN</h3><p>Lorem ipsum dolor sit amet,<br>consectetur adipiscing elit, sed</p></div>

<div class="item keen" style="left:893px;top:207px"><h3>Keen Steps</h3><p>Lorem ipsum dolor sit amet,<br>consectetur adipiscing elit, sed</p></div>
<div class="item curious" style="left:934px;top:340px"><h3>Curious</h3><p>Lorem ipsum dolor sit amet,<br>consectetur adipiscing elit, sed</p></div>
<div class="item gather" style="left:936px;top:462px"><h3>Gather</h3><p>Lorem ipsum dolor sit amet,<br>consectetur adipiscing elit, sed</p></div>
<div class="item move" style="left:936px;top:576px"><h3>Move</h3><p>Lorem ipsum dolor sit amet,<br>consectetur adipiscing elit, sed</p></div>
<div class="item tribe" style="left:892px;top:683px"><h3>Tribe</h3><p>Lorem ipsum dolor sit amet,<br>consectetur adipiscing elit, sed</p></div>
</div>
</body>
</html>
```